Call Center In Need of Website Design

We are a call center that provides inbound and outbound calling & marketing services for eCommerce store. We would like to see a fun, creative, playful design that is simple.

Here are some sample design sites we like;
- https://www.velmorink.com/
- https://tonquel.io/
- https://www.brasklode.com/live-chat-software/
- https://www.quillarbe.com/

Here are some competitor sites;
- https://www.dorvenlinkage.com/
- https://www.helpwaldrix.com/

I have attached website content for your use.
Updates

Target Market(s)

eCommerce

Coding

Coded - Design and coding required

Number of Pages Required

5+ page

Font styles to use
Sans Serif

Colors

Designer to choose colors to be used in the design.

Requirements
Must have
• Must have designs for the following 5 separate pages;
• 1. Home (landing)
• - This will be were the design style really needs to show.
• - Just needs to touch on key services
• - CTA
• 2. About Us
• - Basic page for about me paragraph
• 3. Services
• - List of services with icons
• - Click on service type to expand details or hover over service icon to view popup bubble with details about that service
• 4. Pricing
• - Option to bundle 1(one) digital service plan and 1(one) call center service plan
• - Bundling adds 10% monthly discount to over all price
• - Customer does NOT have to bundle
• - FAQ
• 5. Contact Us
• - Include a capture form (name, company name, email, phone, message)
• - Contact info
• - Business hours
• When customer purchases their desired plan, then they are taken to a page where they must schedule a call with an account rep.
Nice to have
• home page animations
Should not have
• All information on Home/Landing page.

```html
<!DOCTYPE html>
<html lang="en">
<head>
<meta charset="utf-8">
<title>Luneva — Omnichannel Customer Care</title>
<link rel="stylesheet" href="https://fonts.googleapis.com/css2?family=Nunito:wght@400;600;700;800;900&family=Open+Sans:wght@400;600;700&display=swap">
<style>
  :root {
    --teal: #2ec9b2;
    --teal-deep: #1bbba6;
    --teal-tile: #20bca6;
    --teal-soft: #8fe3d6;
    --ink: #111111;
    --grey-text: #7a7a7a;
    --heading-grey: #7d7d7d;
    --panel-grey: #eeeeee;
    --white: #ffffff;
    --footer: #0e0e0e;
    --footer-rule: #333333;
  }
  * { box-sizing: border-box; margin: 0; padding: 0; }
  html, body { width: 730px; height: 1200px; overflow: hidden; }
  body {
    position: relative;
    background: var(--white);
    font-family: "Open Sans", Arial, sans-serif;
    color: var(--ink);
  }
  .abs { position: absolute; }

  /* Hero */
  .hero {
    position: absolute; left: 0; top: 0; width: 730px; height: 408px;
    background: radial-gradient(ellipse at 70% 30%, #39d3bc 0%, var(--teal) 55%, #27bfa8 100%);
  }
  .hero-network {
    position: absolute; left: 470px; top: 55px; width: 160px; height: 150px;
    background: radial-gradient(circle, rgba(20,60,55,.14) 0%, rgba(20,60,55,0) 70%);
  }
  .brand { position: absolute; left: 98px; top: 20px; display: flex; align-items: center; gap: 10px; }
  .brand-dot { width: 30px; height: 30px; border-radius: 50%; border: 2px solid var(--white); }
  .brand-name {
    font-family: "Nunito", Arial, sans-serif; font-weight: 600; font-size: 24px;
    letter-spacing: 4px; color: #5d6b69;
  }
  .top-nav { position: absolute; top: 36px; left: 543px; display: flex; gap: 27px; align-items: center;
    font-family: "Nunito", Arial, sans-serif; font-weight: 800; font-size: 5.5px; color: var(--white); letter-spacing: .3px; }
  .top-nav .link { text-decoration: underline; }
  .menu { display: flex; align-items: center; gap: 5px; }
  .hero-title {
    position: absolute; left: 96px; top: 109px; width: 440px;
    font-family: "Nunito", Arial, sans-serif; font-weight: 900; font-size: 25.5px; line-height: 32px;
    color: var(--white); letter-spacing: .2px;
  }
  .btn-start {
    position: absolute; left: 98px; top: 193px; width: 83px; height: 25px; border-radius: 13px;
    background: var(--white); color: var(--ink);
    font-family: "Nunito", Arial, sans-serif; font-weight: 800; font-size: 6.5px;
    display: flex; align-items: center; justify-content: center; letter-spacing: .2px;
  }
  .hero-copy {
    position: absolute; left: 98px; top: 246px; width: 312px;
    font-size: 8.1px; line-height: 12.8px; color: #173f3a;
  }
  .slide-arrow { position: absolute; top: 200px; }
  .scroll-mark { position: absolute; left: 359px; top: 342px; width: 12px; height: 12px;
    transform: rotate(45deg); background: rgba(255,255,255,.75); }
  .notch { position: absolute; left: 325px; width: 80px; height: 20px; }

  /* What we do */
  .intro-title {
    position: absolute; left: 98px; top: 462px;
    font-family: "Nunito", Arial, sans-serif; font-weight: 800; font-size: 27px; color: var(--heading-grey);
  }
  .intro-title span { color: var(--teal-deep); }
  .intro-copy {
    position: absolute; left: 98px; top: 503px; width: 350px;
    font-size: 7px; line-height: 12.8px; color: var(--grey-text);
  }
  .intro-art {
    position: absolute; left: 465px; top: 458px; width: 148px; height: 94px; border-radius: 6px;
    background: linear-gradient(135deg, var(--teal-soft) 0%, var(--teal-deep) 100%);
  }

  /* Services */
  .services { position: absolute; left: 0; top: 605px; width: 730px; height: 225px; background: var(--panel-grey); }
  .section-label {
    position: absolute; width: 730px; text-align: center;
    font-family: "Nunito", Arial, sans-serif; font-weight: 800; font-size: 7px; letter-spacing: .3px;
  }
  .service-group { position: absolute; top: 666px; width: 207px; height: 125px; border: 1px dashed #c4c4c4; }
  .tile {
    position: absolute; width: 56px; height: 28px; border-radius: 3px; background: var(--teal-tile);
    color: var(--white); font-family: "Nunito", Arial, sans-serif; font-weight: 800; font-size: 5.2px;
    line-height: 6.5px; text-align: center; display: flex; align-items: center; justify-content: center;
    text-transform: uppercase;
  }
  .tile-feature { background: var(--ink); height: 61px; font-size: 7px; line-height: 8.5px; text-transform: none; font-weight: 700; }
  .group-link { position: absolute; left: 334px; top: 728px; width: 62px; border-top: 1px dashed #c4c4c4; }

  /* FAQ */
  .faq { position: absolute; left: 0; top: 830px; width: 730px; height: 173px; background: var(--teal-deep); color: var(--white); }
  .faq-answer {
    position: absolute; left: 100px; top: 900px; width: 530px; text-align: center;
    font-family: "Nunito", Arial, sans-serif; font-weight: 700; font-size: 8.4px; line-height: 14px; color: var(--white);
  }
  .faq-question { position: absolute; width: 730px; top: 937px; text-align: center;
    font-family: "Nunito", Arial, sans-serif; font-weight: 700; font-size: 7.2px; color: var(--ink); }
  .faq-control { position: absolute; top: 962px; width: 16px; height: 16px; border-radius: 2px;
    display: flex; align-items: center; justify-content: center; }
  .faq-prev { left: 346px; background: #0f9484; }
  .faq-next { left: 367px; border: 1px solid var(--white); }

  /* Footer */
  .site-footer { position: absolute; left: 0; top: 1003px; width: 730px; height: 197px; background: var(--footer); color: var(--white); }
  .footer-heading { position: absolute; top: 1019px; font-family: "Nunito", Arial, sans-serif; font-weight: 800; font-size: 5.5px; color: var(--white); }
  .footer-list { position: absolute; left: 98px; top: 1034px; list-style: none; font-size: 6px; line-height: 12.8px; color: var(--white); }
  .footer-social { position: absolute; left: 262px; top: 1034px; font-size: 6px; line-height: 16.5px; }
  .footer-social a { color: var(--white); display: block; text-decoration: underline; }
  .footer-brand { position: absolute; left: 420px; top: 1034px; display: flex; align-items: center; gap: 12px; }
  .footer-brand .brand-dot { width: 38px; height: 38px; border-color: #6fe0cc; }
  .footer-brand .brand-name { font-size: 22px; color: #707070; letter-spacing: 4px; }
  .footer-address { position: absolute; left: 420px; top: 1083px; font-size: 5.8px; line-height: 10px; color: var(--white); font-style: normal; }
  .footer-phone { position: absolute; left: 420px; top: 1107px; display: flex; align-items: center; gap: 6px; font-size: 5.8px; color: var(--white); }
  .footer-rule { position: absolute; left: 98px; top: 1165px; width: 534px; border-top: 1px solid var(--footer-rule); }
  .copyright { position: absolute; left: 98px; top: 1178px; font-size: 5.5px; color: var(--white); }
</style>
</head>
<body>

  <header class="hero">
    <div class="hero-network" role="img" aria-label="Connected-dots network graphic"></div>
    <div class="brand"><span class="brand-dot"></span><span class="brand-name">LUNEVA</span></div>
    <nav class="top-nav">
      <span class="link">HAMBURGER</span>
      <span class="menu">MENU
        <svg width="10" height="7" viewBox="0 0 10 7"><path d="M0 .5h10M0 3.5h10M0 6.5h10" stroke="#fff" stroke-width=".8"/></svg>
      </span>
    </nav>
    <h1 class="hero-title">LUNEVA IS AN OMNICHANNEL PROVIDER FOR CUSTOMER CARE</h1>
    <a class="btn-start">GET STARTED</a>
    <p class="hero-copy">and back-end office support. We primarily work with eCommerce companies around the world. Our service is vital to the core operations and functionality of consumer-focused online eCommerce companies.</p>
    <svg class="slide-arrow" style="left:27px" width="20" height="8" viewBox="0 0 20 8"><path d="M20 4H1M4 1L1 4l3 3" fill="none" stroke="#fff" stroke-width=".9"/></svg>
    <svg class="slide-arrow" style="left:683px" width="20" height="8" viewBox="0 0 20 8"><path d="M0 4h19M16 1l3 3-3 3" fill="none" stroke="#fff" stroke-width=".9"/></svg>
    <div class="scroll-mark"></div>
    <svg class="abs" style="left:364px;top:362px" width="2" height="46"><path d="M1 0v46" stroke="#fff" stroke-width="1"/></svg>
  </header>
  <svg class="notch" style="top:388px" viewBox="0 0 80 20"><path d="M0 20C30 20 38 18 40 0C42 18 50 20 80 20Z" fill="#fff"/></svg>

  <section class="intro">
    <h2 class="intro-title">What <span>Luneva</span> Do</h2>
    <p class="intro-copy">Luneva is your personal customer service &amp; product research team. We love eCommerce, but we love seeing business owners succeed even more! That is exactly why we have developed the processes &amp; technology to take care of the most over looked areas in eCommerce - Customer Service &amp; Retention.</p>
    <div class="intro-art" role="img" aria-label="Illustration of a support agent wearing a headset"></div>
  </section>

  <section class="services">
    <svg class="notch" style="top:0" viewBox="0 0 80 20"><path d="M0 0C30 0 38 2 40 20C42 2 50 0 80 0Z" fill="#fff"/></svg>
  </section>
  <div class="section-label" style="top:641px">LUNEVA SERVICES</div>

  <div class="service-group" style="left:127px"></div>
  <div class="service-group" style="left:396px"></div>
  <div class="group-link"></div>

  <div class="tile" style="left:141.6px;top:681.6px">Email support</div>
  <div class="tile tile-feature" style="left:202.4px;top:681.6px">Digital<br>Services</div>
  <div class="tile" style="left:263.2px;top:681.6px">Product<br>listing</div>
  <div class="tile" style="left:141.6px;top:714.4px">Live chat<br>support</div>
  <div class="tile" style="left:263.2px;top:714.4px">Price<br>monitoring</div>
  <div class="tile" style="left:141.6px;top:748px">Product<br>research</div>
  <div class="tile" style="left:202.4px;top:748px">Click here</div>
  <div class="tile" style="left:263.2px;top:748px">Product photo<br>&amp; video editing</div>

  <div class="tile" style="left:411.2px;top:681.6px">Email support</div>
  <div class="tile tile-feature" style="left:472px;top:681.6px">Call Center<br>Services</div>
  <div class="tile" style="left:532.8px;top:681.6px">Product<br>listing</div>
  <div class="tile" style="left:411.2px;top:714.4px">Live chat<br>support</div>
  <div class="tile" style="left:532.8px;top:714.4px">Price<br>monitoring</div>
  <div class="tile" style="left:411.2px;top:748px">Product<br>research</div>
  <div class="tile" style="left:472px;top:748px">Click here</div>
  <div class="tile" style="left:532.8px;top:748px">Product photo<br>&amp; video editing</div>

  <section class="faq">
    <svg class="notch" style="top:0" viewBox="0 0 80 20"><path d="M0 0C30 0 38 2 40 20C42 2 50 0 80 0Z" fill="#eeeeee"/></svg>
    <svg class="abs" style="left:364px;top:18px" width="2" height="42"><path d="M1 0v42" stroke="#fff" stroke-width="1"/></svg>
  </section>
  <div class="section-label" style="top:878px;color:#fff">FREQUENTLY ASKED QUESTIONS</div>
  <p class="faq-answer">The free trial only relates to the “call center” service packages! There is no hidden fine print or fees to get started. We don't even require any payment info, signatures, or deposits. If you don't like us or our service, just simply walk away.</p>
  <div class="faq-question">Is the free trial really free?</div>
  <div class="faq-control faq-prev"><svg width="5" height="6"><path d="M4 0v6L0 3z" fill="#fff"/></svg></div>
  <div class="faq-control faq-next"><svg width="5" height="6"><path d="M1 0v6l4-3z" fill="#fff"/></svg></div>

  <footer class="site-footer"></footer>
  <div class="footer-heading" style="left:98px">NAVIGATIONS</div>
  <ul class="footer-list">
    <li>- Home</li><li>- About</li><li>- Service</li><li>- Blogs</li><li>- Events</li><li>- Contact Us</li>
  </ul>
  <div class="footer-heading" style="left:262px">FOLLOW US</div>
  <div class="footer-social"><a href="#">Friendlane</a><a href="#">Chirpnet</a></div>
  <div class="footer-heading" style="left:420px">ABOUT</div>
  <div class="footer-brand"><span class="brand-dot"></span><span class="brand-name">LUNEVA</span></div>
  <address class="footer-address">Luneva, Inc.<br>418 Corlin Ave. Ardmere, CA 90000</address>
  <div class="footer-phone">
    <svg width="7" height="12" viewBox="0 0 7 12"><rect x=".5" y=".5" width="6" height="11" rx="1" fill="none" stroke="#fff" stroke-width=".8"/><path d="M2.5 10h2" stroke="#fff" stroke-width=".8"/></svg>
    (800) 555-0147
  </div>
  <div class="footer-rule"></div>
  <div class="copyright">© Copyright 2018 Luneva, All Rights Reserved.</div>

</body>
</html>
```